Digital Album Cover - Where The Quiet River Bends (Piano & Cello)

HiI would like a digital album coverTitle: "Where The Quiet River Bends (Piano & Cello)"Artist: "Lorcan Pettigrew & The Oduya Priscilla"

• Original creativity
• Copyrighted images

```html
<!DOCTYPE html>
<html lang="en">
<head>
<meta charset="utf-8">
<title>Where The Quiet River Bends (Piano &amp; Cello)</title>
<link rel="stylesheet" href="https://fonts.googleapis.com/css2?family=Kalam:wght@400&amp;family=Arimo:wght@400&amp;display=swap">
<style>
  :root {
    --backdrop: #b7b6ba;
    --sleeve-edge: #1b1a1d;
    --sky-top: #3f6ad0;
    --sky-mid: #4a34a8;
    --sky-deep: #3a1e86;
    --sky-bottom: #b424c4;
    --ink: #15101c;
    --artwork-tone: rgba(20, 16, 40, 0.28);
  }
  * { margin: 0; padding: 0; box-sizing: border-box; }
  html, body {
    width: 1200px;
    height: 857px;
    overflow: hidden;
    background: var(--backdrop);
  }
  .canvas {
    position: relative;
    width: 1200px;
    height: 857px;
  }
  .album-cover {
    position: absolute;
    left: 240px;
    top: 68px;
    width: 720px;
    height: 720px;
    background: var(--sleeve-edge);
    padding: 26px;
  }
  .cover-art {
    position: relative;
    width: 100%;
    height: 100%;
    overflow: hidden;
    background:
      radial-gradient(ellipse at 30% 20%, rgba(90, 150, 240, 0.55), transparent 55%),
      radial-gradient(ellipse at 70% 85%, rgba(220, 40, 220, 0.6), transparent 55%),
      linear-gradient(180deg, var(--sky-top) 0%, var(--sky-mid) 40%, var(--sky-deep) 62%, var(--sky-bottom) 100%);
  }
  .artist-name {
    position: absolute;
    top: 34px;
    left: 0;
    right: 0;
    text-align: center;
    font-family: "Arimo", Arial, sans-serif;
    font-size: 17px;
    color: var(--ink);
  }
  .instrument-artwork {
    position: absolute;
    left: 205px;
    top: 84px;
    width: 230px;
    height: 400px;
    border-radius: 46% 46% 40% 40% / 30% 30% 22% 22%;
    background: linear-gradient(180deg, rgba(20, 16, 40, 0.18), var(--artwork-tone));
  }
  .album-title {
    position: absolute;
    top: 502px;
    left: 0;
    right: 0;
    text-align: center;
    font-family: "Kalam", cursive;
    font-size: 32px;
    color: var(--ink);
  }
  .album-subtitle {
    position: absolute;
    top: 552px;
    left: 0;
    right: 0;
    text-align: center;
    font-family: "Kalam", cursive;
    font-size: 21px;
    color: var(--ink);
  }
</style>
</head>
<body>
  <main class="canvas">
    <section class="album-cover">
      <div class="cover-art" role="img" aria-label="Starry purple and blue nebula night sky">
        <p class="artist-name">Lorcan Pettigrew &amp; The Oduya Priscilla</p>
        <div class="instrument-artwork" role="img" aria-label="Line drawing of a cello body combined with piano keys and a bow"></div>
        <h1 class="album-title">Where The Quiet River Bends</h1>
        <p class="album-subtitle">(Piano &amp; Cello)</p>
      </div>
    </section>
  </main>
</body>
</html>
```